Black Granite Web Design Project

We are looking for a design for a new company that will be selling Black Granite slabs and tiles. We will be selling to both end-consumers and granite installers. We have already settled on a logo and hopefully this will give an idea of what we like in our designs. We are not going to be selling online but want people to call us so the site is basically an enhanced business card. We will be focusing a lot on SEO so the design will have to keep that in mind.

We would like to keep the design in 1024x768 to make it easily view-able on all devices.

Regarding navigation there should only be a few sub-pages, like "Granite Slabs", "Granite Tiles", "Delivery", "Contact"

Aside from that we are open to designs. One idea we did have was to personalize the site and have a person there somehow to represent the company, making the user feel there are real people behind this site. This is just an idea and not a must.

The name of the company and site is "Silver Brook Petrano"

Thanks
Updates

Hello All,

Thanks for the great designs. There are some good looking designs that show beautiful kitchens but this site is made for the granite installers and not the retail consumers. So in order not to to confuse the buyers I would like to keep this as much about the raw products as possible. The raw products being the granite slabs, thereby making it obvious we don't sell granite counter tops. 

This design will really be the identity of this company so it is important we get the right message across on this index page and that this page is as complete as possible.

Again, thanks for all the work being put into this.

Target Market(s)

The target audience is granite installers or companies that would with granite slabs.

Industry/Entity Type

Business

```html
<!DOCTYPE html>
<html lang="en">
<head>
<meta charset="utf-8">
<title>Silver Brook Petrano — Granite Tiles</title>
<link rel="stylesheet" href="https://fonts.googleapis.com/css2?family=Arimo:wght@400;700&display=swap">
<style>
  :root {
    --ink: #111111;
    --text: #222222;
    --muted: #8a8a8a;
    --page: #ffffff;
    --band-light: #f3f3f3;
    --band-mid: #e3e3e3;
    --band-dark: #cfcfcf;
    --arrow: #6e6e6e;
    --footer: #000000;
    --link-red: #b0232a;
    --link-blue: #1d4fa0;
    --beige: #ecd9c1;
    --beige-deep: #e2cbae;
    --black-marble: #151515;
    --black-speckle: #232122;
    --slate: #8c8c8c;
  }
  * { box-sizing: border-box; margin: 0; padding: 0; }
  html, body { width: 1200px; height: 1078px; overflow: hidden; }
  body {
    position: relative;
    background: var(--page);
    font-family: "Arimo", Arial, sans-serif;
    color: var(--text);
  }
  .abs { position: absolute; }

  /* header */
  .brand { left: 170px; top: 27px; display: flex; align-items: center; gap: 14px; }
  .brand-mark { width: 22px; height: 22px; background: var(--ink); }
  .brand-name { font-weight: 700; font-size: 27px; color: var(--ink); letter-spacing: -0.3px; }
  .brand-city { left: 206px; top: 60px; font-size: 12px; font-weight: 700; letter-spacing: 2px; color: var(--ink); }

  .main-nav { top: 40px; display: flex; gap: 0; }
  .main-nav a { position: absolute; font-weight: 700; font-size: 16.5px; color: var(--ink); text-decoration: none; white-space: nowrap; }
  .nav-active-bar {
    left: 786px; top: 60px; width: 98px; height: 7px;
    background: repeating-linear-gradient(135deg, #333 0 2px, #888 2px 4px);
  }

  .sub-tabs { top: 102px; }
  .sub-tab { position: absolute; font-weight: 700; font-size: 17px; white-space: nowrap; }
  .sub-tab.active { color: var(--ink); }
  .sub-tab.inactive { color: var(--muted); }
  .tab-square { left: 171px; top: 104px; width: 15px; height: 15px; background: linear-gradient(135deg, #2c3a2f, #0d0d0d); }

  /* gallery band */
  .gallery-band {
    left: 0; top: 132px; width: 1200px; height: 539px;
    background: linear-gradient(180deg, var(--band-mid) 0%, var(--band-light) 8%, var(--band-light) 88%, var(--band-dark) 100%);
  }
  .peek { background: var(--beige); }
  .peek.grey { background: var(--slate); }
  .arrow {
    width: 29px; height: 88px; background: var(--arrow);
    display: flex; align-items: center; justify-content: center;
  }
  .tile { width: 202px; height: 202px; }
  .tile.mineral { background: linear-gradient(135deg, #7f8c93 0%, #5b4a5e 30%, #8e3b3b 45%, #9aa7a8 65%, #6d7b78 100%); }
  .tile.beige { background: linear-gradient(160deg, var(--beige) 0%, var(--beige-deep) 100%); }
  .tile.marble { background: radial-gradient(circle at 70% 30%, #3a3a3a 0%, var(--black-marble) 55%); }
  .tile.speckle { background: var(--black-speckle); }
  .caption { width: 202px; text-align: center; font-weight: 700; font-size: 12.5px; color: var(--text); line-height: 19px; }
  .caption sup { font-size: 7px; }

  /* article */
  .article-title { left: 188px; top: 696px; font-weight: 700; font-size: 16.5px; color: #333; }
  .article-body { left: 172px; top: 723px; width: 862px; font-size: 11.7px; line-height: 16.2px; text-align: justify; color: var(--text); }
  .article-body p { text-indent: 14px; }
  .article-body .red { color: var(--link-red); }
  .article-body .blue { color: var(--link-blue); text-decoration: underline; }

  .share { top: 905px; height: 18px; display: flex; align-items: center; font-size: 10px; }
  .share-btn { height: 18px; padding: 0 5px; display: flex; align-items: center; gap: 4px; background: #eef0f3; border: 1px solid #d9dce1; font-weight: 700; font-size: 10px; color: #333; }
  .share-btn i { width: 9px; height: 9px; display: block; background: #9aa3ad; }
  .share-count { margin: 0 10px 0 9px; color: #333; }

  /* footer */
  .site-footer { left: 0; top: 990px; width: 1200px; height: 88px; background: var(--footer); }
  .footer-brand { left: 182px; top: 1012px; display: flex; flex-direction: column; align-items: center; gap: 5px; width: 118px; }
  .footer-brand .brand-mark { width: 26px; height: 26px; background: #fff; }
  .footer-brand .brand-name { color: #fff; font-size: 11px; white-space: nowrap; }
  .footer-nav a { position: absolute; top: 1023px; color: #fff; font-weight: 700; font-size: 13px; text-decoration: none; white-space: nowrap; }
  .footer-stones { left: 844px; top: 997px; width: 171px; height: 81px; background: linear-gradient(135deg, #1e1e1e 0%, #3a3a3a 50%, #0a0a0a 100%); clip-path: polygon(20% 30%, 60% 0, 100% 15%, 100% 100%, 0 100%, 5% 50%); }
</style>
</head>
<body>

<header>
  <div class="abs brand"><span class="brand-mark"></span><span class="brand-name">SILVER BROOK PETRANO</span></div>
  <div class="abs brand-city">RIO DE JANEIRO</div>
  <nav class="abs main-nav">
    <a style="left:668px">ABOUT US</a>
    <a style="left:790px">DELIVERY</a>
    <a style="left:905px">CONTACTS</a>
  </nav>
  <div class="abs nav-active-bar"></div>
  <div class="abs tab-square"></div>
  <div class="abs sub-tabs">
    <span class="sub-tab active" style="left:193px">GRANITE TILES</span>
    <span class="sub-tab inactive" style="left:373px">GRANITE SLABES</span>
  </div>
</header>

<section class="abs gallery-band" aria-label="Granite tiles"></section>

<div class="abs peek" style="left:0;top:177px;width:153px;height:201px" role="img" aria-label="Beige granite tile, partly hidden"></div>
<div class="abs peek grey" style="left:0;top:388px;width:153px;height:199px" role="img" aria-label="Grey granite tile, partly hidden"></div>
<div class="abs peek" style="left:1045px;top:180px;width:155px;height:202px" role="img" aria-label="Beige granite tile, partly hidden"></div>
<div class="abs peek grey" style="left:1046px;top:392px;width:154px;height:198px" role="img" aria-label="Grey granite tile, partly hidden"></div>

<div class="abs arrow" style="left:142px;top:339px">
  <svg width="12" height="34" viewBox="0 0 12 34"><path d="M10 2 L3 17 L10 32" fill="none" stroke="#fff" stroke-width="3"/></svg>
</div>
<div class="abs arrow" style="left:1029px;top:340px">
  <svg width="12" height="34" viewBox="0 0 12 34"><path d="M2 2 L9 17 L2 32" fill="none" stroke="#fff" stroke-width="3"/></svg>
</div>

<div class="abs tile mineral" style="left:178px;top:154px" role="img" aria-label="Photo of multicoloured granite tile with red and blue veins"></div>
<div class="abs tile beige" style="left:389px;top:154px" role="img" aria-label="Photo of beige veined granite tile"></div>
<div class="abs tile marble" style="left:603px;top:154px" role="img" aria-label="Photo of black granite tile with white veins"></div>
<div class="abs tile speckle" style="left:817px;top:154px" role="img" aria-label="Photo of black speckled granite tile"></div>
<div class="abs caption" style="left:178px;top:361px">Title of a product<br>Price: 300$/m<sup>2</sup></div>
<div class="abs caption" style="left:389px;top:361px">Title of a product<br>Price: 300$/m<sup>2</sup></div>
<div class="abs caption" style="left:603px;top:361px">Title of a product<br>Price: 300$/m<sup>2</sup></div>
<div class="abs caption" style="left:817px;top:361px">Title of a product<br>Price: 300$/m<sup>2</sup></div>

<div class="abs tile mineral" style="left:178px;top:412px" role="img" aria-label="Photo of multicoloured granite tile with red and blue veins"></div>
<div class="abs tile beige" style="left:389px;top:412px" role="img" aria-label="Photo of beige veined granite tile"></div>
<div class="abs tile marble" style="left:603px;top:412px" role="img" aria-label="Photo of black granite tile with white veins"></div>
<div class="abs tile speckle" style="left:817px;top:412px" role="img" aria-label="Photo of black speckled granite tile"></div>
<div class="abs caption" style="left:178px;top:619px">Title of a product<br>Price: 300$/m<sup>2</sup></div>
<div class="abs caption" style="left:389px;top:619px">Title of a product<br>Price: 300$/m<sup>2</sup></div>
<div class="abs caption" style="left:603px;top:619px">Title of a product<br>Price: 300$/m<sup>2</sup></div>
<div class="abs caption" style="left:817px;top:619px">Title of a product<br>Price: 300$/m<sup>2</sup></div>

<article>
  <h1 class="abs article-title">THE TITLE OF ARTICLE OR SEO TEXT</h1>
  <div class="abs article-body">
    <p>Granite /rænt/ is a common type of intrusive, felsic, igneous rock which is granular and phaneritic in texture. This rock consists mainly of quartz, mica, and feldspar. Occasionally some individual crystals (<span class="red">phenocrysts</span>) are larger than the groundmass, in which case the texture is known as porphyritic. A granitic rock with a porphyritic texture is sometimes known as a porphyry. Granites can be pink to gray in color, depending on their chemistry and mineralogy. By definition, granite is an igneous rock with at least 20% quartz by volume. Granite differs from granodiorite in that at least 35% of the feldspar in granite is alkali feldspar as opposed to plagioclase; it is the alkali feldspar that gives many granites a distinctive pink color. Outcrops of granite tend to form tors and rounded massifs. Granites sometimes occur in circular depressions surrounded by a range of hills, formed by the metamorphic aureole or hornfels. Granite is usually found in the continental plates of the Earth's crust.</p>
    <p>Granite is nearly always massive (<span class="blue">lacking internal structures</span>), hard and tough, and therefore it has gained widespread use as a construction stone. The average density of granite is between 2.65[1] and 2.75 g/cm3, its compressive strength usually lies above 200 MPa, and its viscosity near STP is 3-6 • 1019 Pa·s.[2] Melting temperature is 1215 - 1260 °C.</p>
  </div>
  <div class="abs share" style="left:173px">
    <span class="share-btn"><i></i>Tweet</span><span class="share-count">93</span>
    <span class="share-btn"><i></i>Like</span><span class="share-count">1.6m</span>
    <span class="share-btn"><i></i>+1</span>
  </div>
</article>

<footer>
  <div class="abs site-footer"></div>
  <div class="abs footer-brand"><span class="brand-mark"></span><span class="brand-name">SILVER BROOK PETRANO</span></div>
  <nav class="footer-nav">
    <a style="left:339px">GRANITE TILES</a>
    <a style="left:459px">GRANITE&nbsp; SLABES</a>
    <a style="left:598px">ABOUT US</a>
    <a style="left:678px">DELIVERY</a>
    <a style="left:753px">CONTACTS</a>
  </nav>
  <div class="abs footer-stones" role="img" aria-label="Stacked black granite cubes"></div>
</footer>

</body>
</html>
```